Velder Crest is a new and completely innovative health supplement aimed at males between the ages of 25-60.

The supplement is formulated specifically to address two significant factors that affect men as they age. A reduction in the primary sex hormones and a reduction in their fertility.

I already have the logo design and label designed. I am looking to launch the product in January/February following successful trials.
The website won't need to have selling features inbuilt as I will be going through 3rd party platforms.

The website will however need to direct traffic to websites for a couple of purposes. In total I would expect to have in the region of 5-6 pages in total.

```html
<!DOCTYPE html>
<html lang="en">
<head>
<meta charset="utf-8">
<title>Velder Crest — Health Supplement</title>
<link href="https://fonts.googleapis.com/css2?family=Montserrat:wght@400;500;600;700;800;900&family=Roboto:wght@300;400&display=swap" rel="stylesheet">
<style>
:root{
  --blue:#09a6ec;
  --ink:#111111;
  --text:#333333;
  --dark-band:#2b2b2b;
  --light-bg:#f0f1f3;
  --white:#ffffff;
  --field-border:#e3e5e8;
}
*{margin:0;padding:0;box-sizing:border-box}
html,body{width:1200px;height:2758px;overflow:hidden;background:var(--white)}
body{position:relative;font-family:"Montserrat",sans-serif;color:var(--text)}
.abs{position:absolute}
.pill{position:absolute;display:flex;align-items:center;justify-content:space-between;border-radius:40px;color:var(--white);font-family:"Montserrat",sans-serif;font-weight:700;text-transform:uppercase}
.pill .dot{width:32px;height:32px;border-radius:50%;background:var(--white);display:flex;align-items:center;justify-content:center}

/* header */
.brand{left:161px;top:52px;font-size:26px;font-weight:800;color:var(--ink);display:flex;align-items:center;gap:10px}
.brand .mark{width:22px;height:22px;border-radius:50%;background:var(--blue)}
.nav{left:0;top:34px;width:1200px;height:20px}
.nav a{position:absolute;font-size:13px;font-weight:500;color:var(--ink);text-decoration:none}
.nav a.active{color:var(--blue);font-weight:600}

/* hero */
.hero-shape{left:0;top:0}
.hero-kicker{left:160px;top:198px;font-size:23px;font-weight:700;color:var(--blue);letter-spacing:.2px}
.hero-title{left:158px;top:222px;font-size:38px;font-weight:900;color:var(--ink);letter-spacing:.2px}
.hero-lead{left:162px;top:296px;width:560px;font-size:16px;line-height:20px;color:var(--text)}
.checklist{left:161px;top:357px;list-style:none}
.checklist li{display:flex;align-items:center;gap:8px;font-size:12.5px;height:22.5px;color:var(--text)}
.hero-btn{left:161px;top:468px;width:174px;height:43px;background:var(--blue);padding:0 4px 0 22px;font-size:15px}
.hero-product{left:732px;top:126px;width:226px;height:468px;border-radius:40px 40px 30px 30px;background:linear-gradient(180deg,#e8e8e8 0 8%,#c8661c 14%,#f4f4f4 30%,#eef3f8 70%,#b8541a 88%,#8a3d12 100%)}

/* about */
.about-photo{left:161px;top:722px;width:316px;height:295px;border-radius:60px 0 0 0;background:linear-gradient(135deg,#c9a488,#8b6a55 55%,#d9cfc6)}
.about-inset{left:388px;top:924px;width:147px;height:136px;border:4px solid var(--white);box-shadow:0 4px 14px rgba(0,0,0,.18);background:linear-gradient(135deg,#a66f56,#e8dfd2 50%,#46684e)}
.review{left:385px;top:753px;width:152px;height:37px;background:var(--white);box-shadow:0 3px 12px rgba(0,0,0,.15);display:flex;align-items:center;padding:0 8px;gap:6px}
.review .avatar{width:24px;height:24px;border-radius:50%;background:#d8c2b2}
.review .stars{font-size:8px;color:var(--blue);letter-spacing:1px}
.review .name{font-size:7.5px;font-weight:700;color:var(--ink)}
.review .score{position:absolute;right:7px;top:8px;background:var(--blue);color:var(--white);font-size:7px;font-weight:700;padding:1px 6px;border-radius:6px}
.kicker{font-size:23px;font-weight:500;color:var(--blue)}
.section-title{font-size:37px;font-weight:900;color:var(--ink)}
.about-kicker{left:583px;top:725px}
.about-title{left:582px;top:750px}
.about-copy{left:583px;top:808px;width:470px;font-family:"Roboto",sans-serif;font-weight:300;font-size:12.3px;line-height:20.3px;color:#4a4a4a}
.about-btn{left:583px;top:1015px;width:178px;height:43px;background:var(--dark-band);padding:0 5px 0 18px;font-size:16px}

/* products */
.products{left:0;top:1119px;width:1200px;height:631px;background:var(--light-bg)}
.products-kicker{left:0;width:1200px;top:1175px;text-align:center}
.products-title{left:0;width:1200px;top:1199px;text-align:center}
.card{position:absolute;top:1278px;width:272px}
.card .thumb{width:272px;height:236px}
.card h3{margin-top:20px;font-size:15px;font-weight:700;color:#2a2a2a}
.card p{margin-top:9px;font-size:12px;line-height:16.6px;color:#7a7a7a}
.card .pill{position:absolute;top:378px;left:0;width:145px;height:37px;background:var(--blue);padding:0 4px 0 13px;font-size:13px}
.card .pill .dot{width:24px;height:24px}

/* features */
.features{left:0;top:1766px;width:1200px;height:298px;background:var(--dark-band)}
.feature{position:absolute;top:1814px;width:240px;text-align:center;color:var(--white)}
.feature .icon{width:86px;height:86px;margin:0 auto;border-radius:50%;background:var(--white);display:flex;align-items:center;justify-content:center}
.feature h3{margin-top:21px;font-size:19px;font-weight:700}
.feature p{margin-top:4px;font-size:12.5px;line-height:16.5px}
.divider{top:1830px;width:1px;height:167px;background:#5a5a5a}

/* contact */
.map-area{left:150px;top:2130px;width:890px;height:450px;background:radial-gradient(ellipse at center,rgba(220,224,230,.55),rgba(255,255,255,0) 70%)}
.contact-kicker{left:0;width:1200px;top:2122px;text-align:center}
.contact-title{left:0;width:1200px;top:2148px;text-align:center}
.contact-lead{left:310px;top:2207px;width:580px;text-align:center;font-size:12.5px;line-height:21px;color:#555}
.field{position:absolute;background:var(--white);border:1px solid var(--field-border);border-radius:4px;box-shadow:0 2px 5px rgba(0,0,0,.05);font-size:13px;color:#555;padding:18px 22px}
.submit{left:523px;top:2560px;width:152px;height:50px;background:var(--blue);padding:0 10px 0 26px;font-size:19px}

/* footer */
.footer{left:0;top:2674px;width:1200px;height:84px;background:var(--blue)}
.copyright{left:161px;top:2704px;font-size:12px;font-weight:500;color:var(--white)}
.social{top:2694px;width:36px;height:36px;border-radius:50%;border:2px solid var(--white)}
</style>
</head>
<body>

<!-- Header -->
<div class="abs brand"><span class="mark"></span>Velder Crest</div>
<nav class="abs nav">
  <a class="active" style="left:685px">Home</a>
  <a style="left:778px">About us</a>
  <a style="left:892px">Product</a>
  <a style="left:989px">Contact</a>
</nav>

<!-- Hero -->
<svg class="abs hero-shape" width="1200" height="640" viewBox="0 0 1200 640">
  <polygon points="380,632 1200,86 1200,632" fill="var(--blue)"/>
</svg>

<div class="abs hero-kicker">COMPLETELY INNOVATIVE</div>
<h1 class="abs hero-title">HEALTH SUPPLEMENT</h1>
<p class="abs hero-lead">Vanaf 1 maart hebben wij onze nieuwe vestiging Lindmoor Zuid<br>geopend aan het Havenkade 4 te Brelden!</p>
<ul class="abs checklist">
  <li><svg width="13" height="13" viewBox="0 0 13 13"><rect x="1" y="2" width="10" height="10" rx="2" fill="none" stroke="var(--blue)" stroke-width="1.5"/><path d="M3.5 7l2.5 2.5 6-7" fill="none" stroke="var(--blue)" stroke-width="1.8"/></svg>Integer porttitor dui at pharetra rhoncus.</li>
  <li><svg width="13" height="13" viewBox="0 0 13 13"><rect x="1" y="2" width="10" height="10" rx="2" fill="none" stroke="var(--blue)" stroke-width="1.5"/><path d="M3.5 7l2.5 2.5 6-7" fill="none" stroke="var(--blue)" stroke-width="1.8"/></svg>Aliquam eu libero dapibus, sollicitudin ex ut.</li>
  <li><svg width="13" height="13" viewBox="0 0 13 13"><rect x="1" y="2" width="10" height="10" rx="2" fill="none" stroke="var(--blue)" stroke-width="1.5"/><path d="M3.5 7l2.5 2.5 6-7" fill="none" stroke="var(--blue)" stroke-width="1.8"/></svg>Suspendisse ut dolor congue pulvinar.</li>
</ul>
<a class="pill hero-btn">Contact us<span class="dot"><svg width="16" height="16" viewBox="0 0 24 24"><path d="M6.6 10.8a15 15 0 0 0 6.6 6.6l2.2-2.2c.3-.3.7-.4 1-.2 1.1.4 2.3.6 3.6.6.6 0 1 .4 1 1V20c0 .6-.4 1-1 1A17 17 0 0 1 3 4c0-.6.4-1 1-1h3.5c.6 0 1 .4 1 1 0 1.3.2 2.5.6 3.6.1.3 0 .7-.2 1z" fill="var(--blue)"/></svg></span></a>
<div class="abs hero-product" role="img" aria-label="Product photo: amber supplement bottle with white multivitamin label"></div>

<!-- About -->
<div class="abs about-photo" role="img" aria-label="Photo of a woman pouring capsules from a bottle into her hand"></div>
<div class="abs about-inset" role="img" aria-label="Close-up photo of assorted capsules in a palm"></div>
<div class="abs review">
  <span class="avatar"></span>
  <div><div class="stars">★★★☆☆</div><div class="name">MAREN HOLT</div></div>
  <span class="score">4.5</span>
</div>

<div class="abs kicker about-kicker">About Us</div>
<h2 class="abs section-title about-title">VELDER CREST</h2>
<p class="abs about-copy">Lorem ipsum dolor sit amet, consectetur adipiscing elit. Morbi ut purus a turpis dictum laoreet. Suspendisse ac erat odio. Suspendisse sodales viverra nisi, eu sagittis lacus molestie ut. Phasellus porttitor lacus mi. Integer purus dui, aliquet at nisl ac, hendrerit euismod eros. Praesent sit amet semper lectus, et auctor tellus. Nam blandit rutrum libero non elementum. Nullam blandit tempor metus, maximus tincidunt massa iaculis pulvinar. Proin vel lorem pharetra, lobortis mauris ut, interdum augue. Nam sit amet lectus nec odio fringilla dapibus. Nullam blandit tempor metus, maximus tincidunt massa iaculis pulvinar. Proin vel lorem pharetra, lobortis mauris ut, interdum augue. Nam sit amet lectus nec odio fringilla dapibus.</p>
<a class="pill about-btn">Read more<span class="dot"><svg width="14" height="14" viewBox="0 0 14 14"><path d="M2 7h9M7 3l4 4-4 4" fill="none" stroke="var(--dark-band)" stroke-width="2"/></svg></span></a>

<!-- Products -->
<section class="abs products"></section>
<div class="abs kicker products-kicker">Velder Crest</div>
<h2 class="abs section-title products-title">OUR PRODUCT</h2>

<article class="card" style="left:161px">
  <div class="thumb" role="img" aria-label="Product illustration: vitamin jar surrounded by glowing vitamin capsules on teal" style="background:linear-gradient(160deg,#05d3c6,#17b8c6 60%,#0a8fa8)"></div>
  <h3>LORUM IPSLUM DOLAR</h3>
  <p>Lorem ipsum dolor sit amet, consectetur adipiscing elit. Morbi ut purus a turpis dictum laoreet. Suspendisse ac erat odio. uspendisse sodales viverra nisi.</p>
  <a class="pill">View details<span class="dot"><svg width="12" height="12" viewBox="0 0 14 14"><path d="M2 7h9M7 3l4 4-4 4" fill="none" stroke="var(--blue)" stroke-width="2.2"/></svg></span></a>
</article>
<article class="card" style="left:465px">
  <div class="thumb" role="img" aria-label="Product illustration: green multivitamin bottle with floating vitamin spheres on blue" style="background:linear-gradient(180deg,#5cc4ea,#2a93c2 60%,#7ee0f0)"></div>
  <h3>LORUM IPSLUM DOLAR</h3>
  <p>Lorem ipsum dolor sit amet, consectetur adipiscing elit. Morbi ut purus a turpis dictum laoreet. Suspendisse ac erat odio. uspendisse sodales viverra nisi.</p>
  <a class="pill">View details<span class="dot"><svg width="12" height="12" viewBox="0 0 14 14"><path d="M2 7h9M7 3l4 4-4 4" fill="none" stroke="var(--blue)" stroke-width="2.2"/></svg></span></a>
</article>
<article class="card" style="left:768px">
  <div class="thumb" role="img" aria-label="Product illustration: purple vitamin complex jar with colourful vitamin balls on light blue" style="background:linear-gradient(160deg,#8cc6f7,#6aaff0 60%,#b5d8fa)"></div>
  <h3>LORUM IPSLUM DOLAR</h3>
  <p>Lorem ipsum dolor sit amet, consectetur adipiscing elit. Morbi ut purus a turpis dictum laoreet. Suspendisse ac erat odio. uspendisse sodales viverra nisi.</p>
  <a class="pill">View details<span class="dot"><svg width="12" height="12" viewBox="0 0 14 14"><path d="M2 7h9M7 3l4 4-4 4" fill="none" stroke="var(--blue)" stroke-width="2.2"/></svg></span></a>
</article>

<!-- Features -->
<section class="abs features"></section>
<div class="feature" style="left:153px">
  <div class="icon"><svg width="44" height="50" viewBox="0 0 44 50"><circle cx="22" cy="12" r="10" fill="var(--blue)"/><path d="M2 50c0-14 8-22 20-22s20 8 20 22z" fill="var(--blue)"/><path d="M22 28l-3 5 3 14 3-14z" fill="#fff"/></svg></div>
  <h3>Affordable</h3>
  <p>Lorem ipsum dolor sit amet, consectetur adipiscing elit. Praesent ligula lorem.</p>
</div>
<div class="abs divider" style="left:444px"></div>
<div class="feature" style="left:486px">
  <div class="icon"><svg width="46" height="42" viewBox="0 0 46 42"><rect x="2" y="2" width="34" height="24" rx="4" fill="none" stroke="var(--blue)" stroke-width="2.5"/><path d="M10 26v8l8-8" fill="none" stroke="var(--blue)" stroke-width="2.5"/><path d="M36 12h4a4 4 0 0 1 4 4v14a4 4 0 0 1-4 4h-2v6l-7-6H18a4 4 0 0 1-4-4" fill="none" stroke="var(--blue)" stroke-width="2.5"/><circle cx="12" cy="14" r="2" fill="var(--blue)"/><circle cx="19" cy="14" r="2" fill="var(--blue)"/><circle cx="26" cy="14" r="2" fill="var(--blue)"/></svg></div>
  <h3>Chat With Us</h3>
  <p>Lorem ipsum dolor sit amet, consectetur adipiscing elit. Praesent ligula lorem.</p>
</div>
<div class="abs divider" style="left:768px"></div>
<div class="feature" style="left:810px">
  <div class="icon"><svg width="48" height="52" viewBox="0 0 48 52"><path d="M24 2l5 4 6-1 2 6 6 3-2 6 2 6-6 3-2 6-6-1-5 4-5-4-6 1-2-6-6-3 2-6-2-6 6-3 2-6 6 1z" fill="none" stroke="var(--blue)" stroke-width="2.5"/><path d="M16 19l6 6 10-11" fill="none" stroke="var(--blue)" stroke-width="2.8"/><path d="M12 36L6 48l7-2 3 6 6-12M36 36l6 12-7-2-3 6-6-12" fill="none" stroke="var(--blue)" stroke-width="2.5"/></svg></div>
  <h3>Guaranteed</h3>
  <p>Lorem ipsum dolor sit amet, consectetur adipiscing elit. Praesent ligula lorem.</p>
</div>

<!-- Contact -->
<div class="abs map-area" role="img" aria-label="Faint world map background"></div>

<div class="abs kicker contact-kicker">Get in touch</div>
<h2 class="abs section-title contact-title">CONTACT US</h2>
<p class="abs contact-lead">Lorem Ipsum is simply dummy text of the printing and typesetting industry. Lorem Ipsum has been the industry's standard dummy.</p>

<div class="field" style="left:209px;top:2274px;width:383px;height:50px">Name</div>
<div class="field" style="left:608px;top:2274px;width:382px;height:50px">Email</div>
<div class="field" style="left:209px;top:2338px;width:781px;height:50px">Phone</div>
<div class="field" style="left:209px;top:2401px;width:781px;height:119px">Message</div>
<a class="pill submit">Submit<span class="dot" style="width:28px;height:28px"><svg width="12" height="12" viewBox="0 0 14 14"><path d="M2 7h9M7 3l4 4-4 4" fill="none" stroke="var(--blue)" stroke-width="2.2"/></svg></span></a>

<!-- Footer -->
<footer class="abs footer"></footer>
<div class="abs copyright">Copyright © 2023 Velder Crest |&nbsp; All Right Reserved.</div>
<a class="abs social" style="left:924px" aria-label="Social link one"></a>
<a class="abs social" style="left:964px" aria-label="Social link two"></a>
<a class="abs social" style="left:1004px" aria-label="Social link three"></a>

</body>
</html>
```